Painting and decorating services

A flyer that promotes my services as a high quality painter and decorator. My services are fully flexible and we cater for range of customers from the decoration of small homes through to larger businesses. We have the flexibility to work through the night which suits businesses that cannot afford to shut throughout the day. We guarantee a top quality finish and are proud to promote a loyalty scheme for successful referrals.

We are truly a family business that is proud and confident to offer one of the most reliable and friendly services on offer.

Target Market(s)

Family homes, businesses who want offer of 24/7 services

Industry/Entity Type

Painting

Font styles to use
Serif
Sans Serif

Requirements
Must have
• Promotion of reliability, value, quality, service
• Days rates and price work considered
• Promotion of night work
• Loyalty scheme / incentives offerred for referrals
• Concept that we are an extremely hard working team who work extended hours and offer flexibility to customers
• Some picture examples of high quality paint jobs as examples of my work.
• Contact details. Phone 01745382916 or mobile 0762931846 email: tkbrushandfinishworks@mailvane.com
Nice to have
• Notion of friendliness coming across from the advert.
• Commitment to giving the customer what they want and delivering to the highest specifications requested
Should not have
• Any over exaggerated false promises that would make the reader of the flyer believe it's just another blagging tradesman with false marketing and empty promises.

```html
<!DOCTYPE html>
<html lang="en">
<head>
<meta charset="utf-8">
<title>Painter &amp; Decorator Flyer</title>
<link href="https://fonts.googleapis.com/css2?family=Oswald:wght@500;600;700&family=Lato:ital,wght@0,400;0,700;1,400;1,700&display=swap" rel="stylesheet">
<style>
  :root{
    --sky:#5cc6ea;
    --sky-light:#bfe8f7;
    --navy:#0d2a4a;
    --teal:#155f7d;
    --teal-dark:#0f4a63;
    --orange:#f7941d;
    --white:#ffffff;
    --page:#e4e4e4;
  }
  *{box-sizing:border-box;margin:0;padding:0}
  html,body{width:1200px;height:1200px;overflow:hidden;background:var(--page)}
  .flyer{
    position:absolute;left:190px;top:20px;width:820px;height:1160px;
    background:var(--white);overflow:hidden;
    font-family:"Lato",sans-serif;
    box-shadow:0 6px 24px rgba(0,0,0,.18);
  }
  .hero-photo{
    position:absolute;left:0;top:0;width:820px;height:480px;
    background:
      radial-gradient(ellipse 55% 60% at 50% 55%, var(--sky) 0%, rgba(92,198,234,.6) 55%, rgba(255,255,255,0) 80%),
      linear-gradient(180deg,var(--sky-light) 0%, #e9f6fb 100%);
  }
  .logo-badge{
    position:absolute;left:300px;top:28px;width:200px;height:200px;border-radius:50%;
    background:#dff3fb;border:5px solid var(--teal);
    display:flex;flex-direction:column;align-items:center;justify-content:center;
    font-family:"Lato",sans-serif;font-weight:700;color:#111;line-height:1;
  }
  .logo-badge span{font-size:40px}
  .headline{
    position:absolute;left:160px;top:255px;width:520px;text-align:center;
    font-family:"Oswald",sans-serif;font-weight:600;color:var(--navy);line-height:1.2;
  }
  .headline .lead{font-size:38px;display:block}
  .headline .main{font-size:48px;display:block;font-weight:700}
  .services{
    position:absolute;left:0;top:480px;width:520px;height:320px;background:var(--orange);
  }
  .services-title{
    margin:22px 0 0 0;height:64px;background:var(--teal-dark);
    display:flex;align-items:center;padding-left:26px;
    font-family:"Oswald",sans-serif;font-weight:600;font-size:34px;color:var(--white);letter-spacing:.5px;
  }
  .services-title .dot{width:22px;height:22px;border-radius:50%;border:3px solid var(--white);margin-right:14px}
  .services-list{list-style:none;padding:16px 30px 0 46px}
  .services-list li{position:relative;color:var(--navy);font-size:15px;line-height:1.35;margin-bottom:7px}
  .services-list li::before{content:"";position:absolute;left:-16px;top:7px;width:6px;height:6px;border-radius:50%;background:var(--teal)}
  .value{
    position:absolute;left:520px;top:458px;width:300px;height:330px;background:var(--teal);
    padding:28px 26px 0 34px;color:var(--white);
  }
  .value-title{
    display:inline-block;border:2px solid var(--white);padding:4px 14px;
    font-family:"Oswald",sans-serif;font-weight:600;font-size:30px;
  }
  .value-list{list-style:none;margin-top:20px}
  .value-list li{font-size:12.5px;margin-bottom:8px;padding-left:18px;position:relative}
  .value-list li::before{content:"\2605";position:absolute;left:0;top:0;font-size:12px}
  .value-list b{font-weight:700}
  .value-text{font-size:12px;line-height:1.45;margin-top:16px;text-align:justify}
  .work-gallery{position:absolute;left:26px;top:820px;display:flex;gap:8px}
  .work-frame{width:252px;height:170px;background:var(--teal);padding:10px}
  .work-photo{width:100%;height:100%}
  .work-photo.room-one{background:linear-gradient(160deg,#f3ece0 0%,#c8b79c 55%,#8a7358 100%)}
  .work-photo.room-two{background:linear-gradient(160deg,#d9d3c8 0%,#a89c8a 55%,#5e5244 100%)}
  .tools-photo{position:absolute;left:590px;top:815px;width:190px;height:180px;border-radius:12px;
    background:linear-gradient(160deg,#fbd3a0 0%,#f7941d 70%,#e07c10 100%)}
  .tagline{
    position:absolute;left:40px;top:1006px;width:560px;
    font-style:italic;font-size:25px;line-height:1.25;color:var(--teal);
  }
  .contact-bar{
    position:absolute;left:0;top:1080px;width:820px;height:56px;background:var(--orange);
    display:flex;align-items:center;justify-content:space-between;padding:0 26px;
    color:var(--navy);font-size:22px;font-weight:700;
  }
  .contact-item{display:flex;align-items:center;gap:8px}
  .contact-item svg{width:22px;height:22px;flex:none}
  .contact-item.email{font-size:19px}
  .base-band{position:absolute;left:0;top:1136px;width:820px;height:24px;background:var(--teal)}
</style>
</head>
<body>
<main class="flyer">
  <div class="hero-photo" role="img" aria-label="Smiling woman holding a paint roller beside a man rolling sky blue paint onto a white wall"></div>
  <div class="logo-badge"><span>LOGO</span><span>here</span></div>
  <h1 class="headline">
    <span class="lead">Our services as a</span>
    <span class="main">High quality painter</span>
    <span class="main">&amp; Decorator</span>
  </h1>

  <section class="services">
    <h2 class="services-title"><span class="dot"></span>OUR SERVICES :</h2>
    <ul class="services-list">
      <li>Painting and decorating for small family homes through to larger businesses.</li>
      <li>Night work available for businesses that cannot close by day.</li>
      <li>Day rates and price work both considered.</li>
      <li>Careful preparation, filling and wallpapering to the specification you ask for.</li>
      <li>A top quality finish, checked with you before we leave.</li>
      <li>Loyalty rewards for every successful referral.</li>
    </ul>
  </section>

  <section class="value">
    <h2 class="value-title">VaLue &amp; Qulity :</h2>
    <ul class="value-list">
      <li>Day rates - <b>Ask for a quote</b></li>
      <li>Price work - <b>Fixed quotes</b></li>
      <li>Night &amp; weekend work - <b>Available</b></li>
      <li>Referrals - <b>Loyalty reward</b></li>
    </ul>
    <p class="value-text">We are a friendly family business, proud to offer a reliable service. Tell us what you want and we will work to the specification you ask for, at a fair price and at a time that suits you. Recommend us to a friend and we will thank you with a reward.</p>
  </section>

  <div class="work-gallery">
    <div class="work-frame"><div class="work-photo room-one" role="img" aria-label="Freshly decorated bright living room with cream walls and bay windows"></div></div>
    <div class="work-frame"><div class="work-photo room-two" role="img" aria-label="Finished lounge with neutral painted walls, sofa and framed pictures"></div></div>
  </div>
  <div class="tools-photo" role="img" aria-label="Orange paint bucket with a paint roller resting on it"></div>

  <p class="tagline">We are an extremely hard working team who work extended hours and offer flexibility to customers</p>

  <footer class="contact-bar">
    <span class="contact-item">
      <svg viewBox="0 0 24 24" fill="none" stroke="#ffffff" stroke-width="2"><circle cx="12" cy="12" r="10"/><path d="M9 7.5c-.8.5-1 1.5-.5 2.8a10 10 0 0 0 5.2 5.2c1.3.5 2.3.3 2.8-.5l-1.8-1.5-1.2.8a6 6 0 0 1-2.8-2.8l.8-1.2z" fill="#ffffff" stroke="none"/></svg>
      01745382916
    </span>
    <span class="contact-item">
      <svg viewBox="0 0 24 24" fill="none" stroke="#ffffff" stroke-width="2"><rect x="7" y="2" width="10" height="20" rx="2"/><line x1="10" y1="18" x2="14" y2="18"/></svg>
      0762931846
    </span>
    <span class="contact-item email">
      <svg viewBox="0 0 24 24" fill="none" stroke="#ffffff" stroke-width="2"><rect x="2" y="5" width="20" height="14" rx="1"/><path d="M2 6l10 7 10-7"/></svg>
      tkbrushandfinishworks@mailvane.com
    </span>
  </footer>
  <div class="base-band"></div>
</main>
</body>
</html>
```